Norwegian Mobile Home/Cabin Producer Needs Brochure Design

We make and deliver our own brand of mobile homes especially made for Norway and it's weather conditions. We differ from other brands in building quality in regards to a much more solid construction, insulation and choices. We work with our customer from the beginning and build them after their demands and wishes.
We need a brochure that holds us out as top of the line. We deliver mobile homes of all kinds and sizes. Both to the private and professional sector.
For the professional sector, mainly camping sites we want to show, lodges-, sanitary- and kitchen wagoons etc.
So we need a brochure of 14-20 pages in A4 where the double pages can be printed in A3 format.
We have logo (provided). But we need cover as well as back suggestions.
It should start with pages where we can teel who we are and stand for.Piicture(s) and space for some editable text (which we can write in norwegian). The text part can have a transparent background......or not. Give us your best shot. Also a smaller part in the private sector that shows winter time.
We want other pages for the private sector that shows what we deliver and the possibilities of choices.
Pages for the the professional sector.
Pages that show our production. How we transport. And the split construction. Only pictures from this portfolio here. (see fotoskap portfolios)
Take a look at provided pictures and our website www.solvikhytta.no for inspiration.
Here's a FotoSkap link to Pictures to choose from. http://bildelagr.example/K4TQ9P
(Hope it Works, let me know if not)
Our company name in small letters "fjordgrønn hyttebygg" means directly translated "fjordgreen cabin builds".
Looking forward to your suggestions.
Target Market(s)
Private market for vacation mobile homes. Camping sites and similar
Industry/Entity Type
Insulation
Requirements
Must have
- Our logo on the front page. Simple but inviting and professional
Logo and address on the back.

```html
<!DOCTYPE html>
<html lang="en">
<head>
<meta charset="utf-8">
<title>fjordgrønn hyttebygg – mobile homes brochure cover</title>
<link rel="stylesheet" href="https://fonts.googleapis.com/css2?family=Open+Sans:wght@300;400;600&family=Open+Sans+Condensed:wght@300&display=swap">
<style>
  :root {
    --brand-red: #d9261c;
    --panel-black: #0b0b0b;
    --divider-red: #e0261b;
    --rule-grey: #8c8c8c;
    --rule-light: #f1b3ae;
    --watermark-red: #e4625a;
    --ink-white: #ffffff;
    --photo-patio: #8d9a8e;
    --photo-interior: #8a5a36;
    --photo-cabin: #9b5b4c;
    --photo-hall: #b9bcbc;
    --photo-truck: #8e9a80;
  }
  html, body { margin: 0; padding: 0; overflow: hidden; background: #ffffff; }
  .cover {
    position: relative;
    width: 851px;
    height: 1200px;
    overflow: hidden;
    background: var(--brand-red);
    font-family: "Open Sans", Arial, sans-serif;
    color: var(--ink-white);
  }
  .abs { position: absolute; }
  .panel-black { left: 202px; top: 0; width: 385px; height: 1200px; background: var(--panel-black); }
  .divider { left: 390px; top: 0; width: 6px; height: 1068px; background: var(--divider-red); }
  .rule { height: 1px; background: var(--rule-grey); }
  .rule.light { background: var(--rule-light); }
  .watermark { left: 0; top: 0; }
  .photo { display: block; }
  .photo-patio { left: 202px; top: 54px; width: 187px; height: 93px; background: linear-gradient(160deg, #c9d2d0, var(--photo-patio) 60%, #5d6a5a); }
  .photo-frame { left: 396px; top: 176px; width: 161px; height: 208px; border: 1px solid #bdbdbd; box-sizing: border-box; }
  .photo-interior { left: 396px; top: 196px; width: 158px; height: 188px; background: linear-gradient(180deg, #b88658, var(--photo-interior) 55%, #3e2416); }
  .photo-cabin { left: 396px; top: 433px; width: 135px; height: 215px; background: linear-gradient(180deg, #9aa1a6 0 18%, var(--photo-cabin) 18% 70%, #a98a5e 70%); }
  .photo-hall { left: 396px; top: 700px; width: 189px; height: 132px; background: linear-gradient(180deg, #5a5d60, var(--photo-hall) 40%, #8b8e8c); }
  .photo-truck { left: 396px; top: 917px; width: 189px; height: 149px; background: linear-gradient(180deg, #d3d6d2, var(--photo-truck) 45%, #6c7561); }
  .sector-label {
    font-family: "Open Sans Condensed", "Open Sans", sans-serif;
    font-weight: 300;
    font-size: 21px;
    line-height: 1;
    white-space: nowrap;
    writing-mode: vertical-rl;
    transform: rotate(180deg);
  }
  .label-private { left: 363px; top: 264px; }
  .label-professional { left: 216px; top: 470px; }
  .label-production { left: 363px; top: 682px; }
  .label-transport { left: 216px; top: 924px; }
  .tagline-box {
    left: 656px; top: 496px; width: 121px; height: 229px;
    border: 1px solid var(--ink-white); box-sizing: border-box;
    display: flex; flex-direction: column; align-items: flex-end; justify-content: center;
    padding-right: 8px; line-height: 0.95;
  }
  .tagline-box span { display: block; }
  .tag-we { font-size: 60px; font-weight: 400; letter-spacing: -2px; }
  .tag-implement { font-size: 22px; font-weight: 400; margin-bottom: 4px; }
  .tag-your { font-size: 56px; font-weight: 400; letter-spacing: -2px; }
  .tag-designs { font-size: 28px; font-weight: 400; margin-top: 4px; }
  .company-name {
    left: 210px; top: 1084px; width: 376px;
    font-size: 35px; font-weight: 400; letter-spacing: 0.5px; white-space: nowrap;
  }
</style>
</head>
<body>
  <main class="cover">
    <svg class="abs watermark" width="851" height="1200" viewBox="0 0 851 1200" aria-hidden="true">
      <text x="-1174" y="198" transform="rotate(-90)" textLength="1060" lengthAdjust="spacingAndGlyphs"
            font-family="Open Sans, sans-serif" font-weight="300" font-size="205" fill="var(--watermark-red)">mobile homes</text>
    </svg>

    <div class="abs panel-black"></div>
    <div class="abs divider"></div>

    <div class="abs rule" style="left:22px; top:663px; width:180px;"></div>
    <div class="abs rule" style="left:202px; top:242px; width:187px;"></div>
    <div class="abs rule light" style="left:587px; top:411px; width:246px;"></div>
    <div class="abs rule light" style="left:396px; top:895px; width:437px;"></div>

    <div class="abs photo photo-patio" role="img" aria-label="Photo: mobile home terrace with table, chairs and potted plants"></div>
    <div class="abs photo-frame"></div>
    <div class="abs photo photo-interior" role="img" aria-label="Photo: warm-lit mobile home interior with sofa and kitchen"></div>
    <div class="abs photo photo-cabin" role="img" aria-label="Photo: red cabin with white porch railing and grey roof"></div>
    <div class="abs photo photo-hall" role="img" aria-label="Photo: white mobile home under construction in a production hall"></div>
    <div class="abs photo photo-truck" role="img" aria-label="Photo: pickup truck towing a mobile home"></div>

    <div class="abs sector-label label-private">Private Sector</div>
    <div class="abs sector-label label-professional">Professional Sector</div>
    <div class="abs sector-label label-production">Production Sector</div>
    <div class="abs sector-label label-transport">Transport Sector</div>

    <div class="abs tagline-box">
      <span class="tag-we">We</span>
      <span class="tag-implement">implement</span>
      <span class="tag-your">your</span>
      <span class="tag-designs">designs</span>
    </div>

    <div class="abs company-name">fjordgrønn hyttebygg as</div>
  </main>
</body>
</html>
```